flat health bread wrap

PREFERENCE WILL BE GIVEN TO DESIGNERS WHO CAN SUBMIT THEIR INITIAL IDEAS PRIOR TO 9.00AM FRIDAY 12TH AUGUST 2010 MELBOURNE AUSTRALIA TIME!

additonal packaging information

target market:

mothers who make their childrens lunch, people looking for a healthy alternative and a change to normal bread,

pack size

34cm length X 28.5cm width
crystal-clear, see through plastic re-sealable zip lock pack.

brand name: tidy fold
product explanation: mediterranean flat bread
product features: see below
raw product size: 22cm X 22cm SQUARE
most US products of this style are round or oval! ours will be new to the US market.
colour: pale pita bread colour
markings on bread: pale fried hotplate markings
number of pieces per pack: 8
gross weight of product 250 grams
product manufactured in melbourne australia
accreditations: kosher and halal

front of pack: good design and accreditations (KOSHER AND HALAL)

back of pack: barcode, how to wrap instructions,
US nutritional panel, ingredient list (flour, water, salt and vitamins. gluten allegen warning. oxygen absorbing sachet warning (do not eat)
company address and contact details,

3 flavours: Rye, White, wholmeal and Corn.

marketing
new product designed specificaly for the US market,
distribution: supermarkets, health food stores
retail price: USD $2.99

# New Middle Eastern style Healthy Valley Loaf Wraps. (Tortillas)
# Square flat bread sheets
# For distribution across USA
# Targetting
* Health food enthusiats
* New Age consumers
* Mothers looking for lunchbox options
* Those seeking a substitute for the traditional lunch sandwich
* These square flat bread sheets replace the traditional bread made sandwich

These products are:
# Shelf stable (minimum 6 months) without refrigeration
# Completely free of:
- preservatives
- colours
- yeast
- cholesterol
- trans fats
- hydrogenated oils
# soft and pliable, and extremely thin
# made from wheat/rye/corn flour, water and salt AND NOTHING ELSE
# organic and other options available
# manufactured in Melbourne Australia
# Kosher and Halal certified

Our proposed brand name is TIDY FOLD
# we prefer to dwell on the humourous perspectives of the name
# our product will look something like these - http://www.valleyloaf.com.au/cgi-bin/index.pl?menu_id=3
and these http://www.sunridgeovens.com.au/tavi.html

# This range is unique
in that it is without additives preservatives etc
is NOT round but square in shape
^ we wouold like to emphasise this
^ packaged in transparent zip-lock bags

Reason: we would like to have a better idea of our package design for our meeting 9.00am friday 12th august. MELBOURNE AUSTRALIA TIME!

dear norah,

we have already guaranteed $260.00. 

we expect to spend about $1,000-1,500 for this design project by the time we have accepted someone from the contest.

things that still need to be completed in 4 flavours...... and we will pay for! 
1. barcode
2. text
3. US nutritional panel
4. how to wrap instructions
5. ingredient lists
6. etc.
It's not about the money, money, money,
We don't need your money, money, money.
We just wanna make the world dance,
Forget about the paper moon.
Ain't about the (ha!) cha-ching cha-ching.
Ain't about the (yeah!) ba-bling ba-bling,
Wanna make the world dance,

Read more: http://artists.tunecorner.com/rosa-k-lyrics-paper-moon-feat-lu-t-xk52mrw#ixzz9R2KtPq0b 
TuneCorner - Your favorite Music Community 

desmond

Reason: only 5 designers (16 designs) have submitted work for assessment out of 37,000! I will award contest at the end of the extended 7 days desmond

Reason: because I can and the entries received to date are un satisfactory! desmond

Target Market(s)

our competitors in australia. see there packs in the links below

http://www.valleyloaf.com.au
http://www.pelicor.com.au/wv_softwraps.aspx
http://www.tqgfoods.com.au/nuvora2/index.php?option=com_zoo&view=item&Itemid=204

Industry/Entity Type

It Company

Requirements
Must have

• i FORGOT, THE PRODUCT IS DISPLAYED IN 2 WAYS

1. ABOVE THE ZIP LOCK CLOSE TO THE TOP 2 CORNERS ARE HANGING HOLES. THE PRODUCT SWINGS FROM 2 HOOKS IN A SUPER MARKET

2. THE PRODUCT IS STACKED. ONE ON TOP OF THE OTHER.

IN A SHELF
Nice to have
• HEALTHY, GREEN COLOURS, BROWNS, CREAMS, SOFT FONTS, LOGO OR SYMBOL? i DO NOT REALLY KNOW!
Should not have
• BRIGHT COLOURS! SCREAMING HEADLINES!

KEEP IN MIND THE SQUARE SHAPE PRODUCT AND THE PRODUCT COLOUR WILL BE SEEN THROUGH THE CLEAR PACK

```html
<!DOCTYPE html>
<html lang="en">
<head>
<meta charset="utf-8">
<title>tidy fold – mediterranean flat bread pack</title>
<link rel="stylesheet" href="https://fonts.googleapis.com/css2?family=Alegreya+Sans:ital,wght@1,400&family=Source+Sans+3:wght@300;400;700&family=Arimo:wght@400;700;900&display=swap">
<style>
  :root {
    --stage: #e9e7e2;
    --pack-edge: #8fc54a;
    --pack-mid: #b1bf86;
    --pack-soft: #b7c192;
    --ink-dark-green: #2f7d2a;
    --ink-white: #ffffff;
    --ink-black: #111111;
    --panel-white: #ffffff;
  }
  * { box-sizing: border-box; margin: 0; padding: 0; }
  html, body { width: 1200px; height: 848px; overflow: hidden; }
  body {
    background: var(--stage);
    position: relative;
    font-family: "Source Sans 3", sans-serif;
  }
  .label {
    position: absolute;
    top: 95px;
    width: 362px;
    height: 634px;
    overflow: hidden;
  }
  .label--front {
    left: 254px;
    background: linear-gradient(90deg, var(--pack-edge) 0%, #a6c36d 18%, var(--pack-mid) 45%, var(--pack-soft) 70%, #a3c667 90%, var(--pack-edge) 100%);
  }
  .label--back {
    left: 770px;
    width: 355px;
    background: linear-gradient(90deg, #a7c46f 0%, var(--pack-mid) 30%, var(--pack-soft) 65%, #a4c569 90%, var(--pack-edge) 100%);
  }
  .swoosh { position: absolute; left: 0; top: 0; }

  .accreditation {
    position: absolute; left: 33px; top: 22px;
    font-size: 12px; color: var(--ink-white);
  }
  .flavour {
    position: absolute; right: 18px; top: 14px;
    font-family: "Alegreya Sans", sans-serif; font-style: italic;
    font-size: 34px; color: var(--ink-dark-green);
  }
  .brand-name {
    position: absolute; left: 40px; top: 200px;
    font-weight: 300; color: var(--ink-white);
    font-size: 96px; line-height: 0.95;
    letter-spacing: 1px;
  }
  .product-line {
    position: absolute; left: 0; right: 0; top: 588px;
    text-align: center;
    font-size: 20px; color: var(--ink-dark-green);
  }

  .price {
    position: absolute; left: 19px; top: 20px;
    font-size: 23px; color: var(--ink-white);
  }
  .features {
    position: absolute; left: 19px; top: 117px; width: 180px;
    font-size: 7.6px; line-height: 1.45; color: var(--ink-black);
    list-style: none;
  }
  .fold-steps {
    position: absolute; left: 19px; top: 272px; width: 180px;
    font-size: 8px; line-height: 1.55; color: var(--ink-black);
  }
  .origin {
    position: absolute; left: 19px; top: 408px;
    font-family: "Arimo", sans-serif; font-weight: 700;
    font-size: 14.5px; line-height: 1.25; color: var(--ink-black);
  }
  .code-space {
    position: absolute; left: 19px; top: 541px;
    width: 150px; height: 60px; background: var(--panel-white);
  }
  .net-weight {
    position: absolute; left: 234px; top: 592px;
    font-size: 14px; color: var(--ink-black);
  }
  .recycle-mark {
    position: absolute; left: 318px; top: 583px;
  }

  .nutrition {
    position: absolute; left: 202px; top: 112px; width: 122px;
    background: var(--panel-white);
    border: 1px solid var(--ink-black);
    padding: 3px 4px 4px;
    font-family: "Arimo", sans-serif; color: var(--ink-black);
    font-size: 6.2px; line-height: 1.35;
  }
  .nutrition__title { font-weight: 900; font-size: 15px; line-height: 1; }
  .nutrition__row { display: flex; justify-content: space-between; border-top: 0.6px solid var(--ink-black); }
  .nutrition__row--indent { padding-left: 6px; }
  .nutrition__row b { font-weight: 700; }
  .nutrition__rule { height: 5px; background: var(--ink-black); margin: 1px 0; }
  .nutrition__rule--thin { height: 2.5px; }
  .nutrition__note { font-size: 4.6px; line-height: 1.3; border-top: 0.6px solid var(--ink-black); padding-top: 1px; }
</style>
</head>
<body>

<section class="label label--front" aria-label="Front label">
  <svg class="swoosh" width="362" height="634" viewBox="0 0 362 634" aria-hidden="true">
    <path d="M120 48 C190 28 270 26 362 36 L362 42 C280 34 200 36 120 48 Z" fill="#ffffff" opacity="0.55"/>
  </svg>
  <p class="accreditation">Kosher and Halal</p>
  <p class="flavour">white</p>
  <h1 class="brand-name">tidy<br>fold</h1>
  <p class="product-line">mediterranean flat bread</p>
</section>

<section class="label label--back" aria-label="Back label">
  <svg class="swoosh" width="355" height="634" viewBox="0 0 355 634" aria-hidden="true">
    <path d="M0 68 C70 58 140 62 180 84 C140 70 70 66 0 74 Z" fill="#ffffff" opacity="0.6"/>
  </svg>
  <p class="price">$ 2.99</p>

  <ul class="features">
    <li>Shelf stable (minimum 6 months) without refrigeration</li>
    <li>Completely free of:</li>
    <li>- preservatives</li>
    <li>- colours</li>
    <li>- yeast</li>
    <li>- cholesterol</li>
    <li>- trans fats</li>
    <li>- hydrogenated oils</li>
    <li>Soft and pliable, and extremely thin</li>
    <li>Made from wheat/rye/corn flour, water and salt</li>
    <li>AND NOTHING ELSE</li>
  </ul>

  <div class="fold-steps">
    <p>How to fold instructions:</p>
    <p>Add ingredients on to the bread.</p>
    <p>Fold flat bread and tightly roll up.</p>
  </div>

  <div class="nutrition" aria-label="Nutrition Facts">
    <p class="nutrition__title">Nutrition Facts</p>
    <p>Serving Size 1/2 cup (about 82g)</p>
    <p>Servings Per Container 8</p>
    <div class="nutrition__rule"></div>
    <p>Amount Per Serving</p>
    <div class="nutrition__row"><span><b>Calories</b> 200</span><span>Calories from Fat 130</span></div>
    <div class="nutrition__rule nutrition__rule--thin"></div>
    <div class="nutrition__row"><span></span><span>% Daily Value*</span></div>
    <div class="nutrition__row"><span><b>Total Fat</b> 14g</span><b>22%</b></div>
    <div class="nutrition__row nutrition__row--indent"><span>Saturated Fat 9g</span><b>45%</b></div>
    <div class="nutrition__row nutrition__row--indent"><span>Trans Fat 0g</span><span></span></div>
    <div class="nutrition__row"><span><b>Cholesterol</b> 55mg</span><b>18%</b></div>
    <div class="nutrition__row"><span><b>Sodium</b> 40mg</span><b>2%</b></div>
    <div class="nutrition__row"><span><b>Total Carbohydrate</b> 17g</span><b>6%</b></div>
    <div class="nutrition__row nutrition__row--indent"><span>Dietary Fiber 1g</span><b>4%</b></div>
    <div class="nutrition__row nutrition__row--indent"><span>Sugars 14g</span><span></span></div>
    <div class="nutrition__row"><span><b>Protein</b> 3g</span><span></span></div>
    <div class="nutrition__rule"></div>
    <div class="nutrition__row"><span>Vitamin A 10%</span><span>• Vitamin C 0%</span></div>
    <div class="nutrition__row"><span>Calcium 10%</span><span>• Iron 6%</span></div>
    <p class="nutrition__note">*Percent Daily Values are based on a 2,000 calorie diet. Your daily values may be higher or lower depending on your calorie needs.<br>
    Total Fat less than 65g 80g · Sat Fat less than 20g 25g · Cholesterol less than 300mg · Sodium less than 2,400mg · Total Carbohydrate 300g 375g · Dietary Fiber 25g 30g<br>
    Calories per gram: Fat 9 • Carbohydrate 4 • Protein 4</p>
  </div>

  <p class="origin">Product manufactured:<br>Melbourne Australia</p>
  <div class="code-space" aria-hidden="true"></div>
  <p class="net-weight">250 gr</p>
  <svg class="recycle-mark" width="22" height="22" viewBox="0 0 22 22" aria-label="Recyclable">
    <circle cx="11" cy="11" r="9" fill="#3f9c35"/>
  </svg>
</section>

</body>
</html>
```